Yoga/movement guide/teacher for adult yoga practice and kid yoga

What is the positioning or mission statement of your company? to guide individuals in a yoga-based safe and sustainable movement practice applicable to all ages and body types. Currently my focus is working with children in daycare and school settings, but my goal is to expand into private yoga practice for adults, and potentially as part of rented space in studios. I hope to find a way to work with children AND adults (so would love for logo to be appealing to both), but current focus is with children based on need and demand in the community. yoga for children also compliments my backround as a pediatrician/neonatologist, and I greatly miss interacting with children. I also want to emphasize a yoga/movement practice that is focused more on what one feels internally through movement. NOT what one looks like asthetically. I believe in removing all mirrors from yoga/movement practice. It should be an experience of movement/poses/yoga through appropriate cueing and education. It is not about the details of how far the knee should bend, or how high the leg should be. Focusing on foudation first, core, then core engagement and ultimately expression of poses/movements. A focus on strength, stability and mobility, not just flexibility, which is the common perception/association with yoga. I also want individuals to learn to be an advocate of their own health. Through guidance, I hope for individuals to connect with their body so they know themselves so well to be able to advocate for themselves in the modern healthcare world. This internal experience and connection is so essential in a world where modern medicine has become a business and it is all about making a dollar. the connection with patients is lost, and individuals need to learn to empower themselves and through their new found voice to be able to articulate what is wrong.<br/>Does your company have a tagline or slogan that should be included with the logo? "Find Your Inner Motion"<br/>What do you hope your company can be known for? Accessible yoga for a sustained practice. A guided movement practice where one gains information and knowledge of oneself through a mind/body connection. For one feel good physically with a new awaraness of their internal radiance that exists in all beings. Physical rejuvenation egnites a light and increases energy to flow through the physical body, which ultimately tranlates into works of kindness for others and out in the world. <br/>What color palettes might you prefer? why? love the colors currently chosen<br/>Where will the logo be primarily used? initially business cards, but hopefully future websites, t-shirts, and potentially local magazine adds. Also starting with a small couple of banners for community events in the area. I currently practice as a nomad out of my car :)<br/>Are there any elements you would prefer to see in the logo? Movement. A modern depiction of a human body/figure practicing movement. Hoping to avoid a stereotypical yoga pose per say, just because I want to people to think of it more of a movement practice with yoga roots. Modern yoga. There are elements of breathing and connecting with oneself through the flow of breath and movement, but I do not focus on the meditative/cerebral aspect of the yoga practice. What I teach is almost reaching a meditative state through movement. I personally don't practice, nor resonate with just seated meditation. just not my thing :)<br/>In your opinion, what defines a well-designed logo? curiosity. enough info for individuals to think they know what it means, but want to know more. invokes curiosity, but not too abstract. Reproducible. not too complicated. I want also to invoke a community feel, so a design that appeals to all people within a community. <br/>What is your preference in reference to icons, typography, spokespeople (characters), etc.? modern design. I love the idea of a logo for my purposes, to invoke a sense of movement from within. So not too static. <br/>What words or icons must be included in the logo? movement with yoga roots. <br/>What logos do you like and why? A representation, but not exact. I think some ambiguity is intriguing for others, and also memorable. I want it to be an artistic representation of movement/yoga<br/>What logos do you dislike and why? too busy, too loud. <br/>In your opinion, what is the primary purpose for a logo? association<br/>Who is the primary target audience? (who is most likely to use your services/product?) Children and their parents, but ultimately to expand into teaching adults. I even have aspirations of prenatal and post-natal yoga. Potentially incorporating infants. <br/>Who currently uses your product the most? n/a (working in schools/daycare currently. It is currently all volunteer)<br/>Are you pleased with the range of people your company serves? n/a<br/>Are you looking to expand, modify, or completely change your target audience? or will it remain the same? yes! expand into an adult audience. <br/>How do you plan to focus on your target audience? currently by working through schools and daycares. hopefully ultimately through after school care programs and then offering kid yoga in an existing yoga studio (working on this with Quillbrook in Ridgeland, currently)<br/>What are your main forms of advertising? word of mouth, schools, daycares. Happy kids talking to their parents about the yoga class they took and happy teachers :)<br/>How do most customers find out about your company?<br/>Which gender are you targeting? All genders! However, with kid yoga, often the maternal individual in the child's life is more involved with decision making as far as extracurricular activities

Target Market(s)

individuals and families interested in wellness and feeling great

Contact Information for Business Card

Dana Whitford
Yoga Instructor
RYT-200, RCYT

certified yoga teacher for adults and children

Colors

Requirements
Must have
• "Find Your Inner Motion"
Nice to have
• logo with same colors

```html
<!DOCTYPE html>
<html lang="en">
<head>
<meta charset="utf-8">
<title>Brightloom Studios – Business Card</title>
<link rel="stylesheet" href="https://fonts.googleapis.com/css2?family=Arimo:wght@400;700&family=Indie+Flower&display=swap">
<style>
  :root {
    --stage: #1c1c1c;
    --card: #33373a;
    --card-deep: #2c3033;
    --pattern: #3b3f42;
    --sun: #f6d93a;
    --aqua: #5ec9d1;
    --ink: #f2f2f2;
    --muted: #9aa0a4;
  }
  * { box-sizing: border-box; margin: 0; padding: 0; }
  html, body {
    width: 1200px; height: 900px; overflow: hidden;
    background: var(--stage);
    font-family: "Arimo", Arial, sans-serif;
  }
  .canvas {
    position: relative; width: 1200px; height: 900px;
    display: flex; flex-direction: column; align-items: center; justify-content: center; gap: 34px;
  }
  .card {
    position: relative; width: 700px; height: 400px;
    background: var(--card); overflow: hidden;
  }
  /* back side */
  .card-back .pattern {
    position: absolute; inset: 0;
    background: radial-gradient(ellipse at 50% 50%, var(--card) 0%, var(--pattern) 60%, var(--card-deep) 100%);
  }
  .brand-lockup {
    position: absolute; display: flex; align-items: center; gap: 14px; white-space: nowrap;
  }
  .card-back .brand-lockup {
    left: 50%; top: 50%; transform: translate(-50%, -50%);
  }
  .brand-mark {
    border-radius: 50%; background: var(--sun); flex: none;
  }
  .card-back .brand-mark { width: 120px; height: 120px; }
  .brand-name {
    font-family: "Arimo", Arial, sans-serif; font-weight: 400; color: var(--muted);
    letter-spacing: 1px; white-space: nowrap;
  }
  .card-back .brand-name { font-size: 32px; }

  /* front side */
  .card-front .brand-lockup { left: 70px; top: 30px; }
  .card-front .brand-mark { width: 100px; height: 100px; }
  .card-front .brand-name { font-size: 26px; }
  .tagline {
    position: absolute; left: 186px; top: 112px; white-space: nowrap;
    font-size: 10px; letter-spacing: 2px; text-transform: uppercase; color: var(--aqua);
  }
  .accent-bar {
    position: absolute; left: 42px; top: 194px; width: 5px; height: 50px; background: var(--aqua);
  }
  .person-name {
    position: absolute; left: 62px; top: 180px; white-space: nowrap;
    font-family: "Indie Flower", cursive; font-weight: 400; font-size: 40px; line-height: 48px;
    color: var(--sun); letter-spacing: 1px;
  }
  .person-role {
    position: absolute; left: 62px; top: 232px; font-size: 20px; line-height: 24px; color: var(--ink);
  }
  .divider {
    position: absolute; left: 56px; right: 40px; top: 276px; height: 1px; background: var(--aqua);
  }
  .contact-list {
    position: absolute; left: 44px; top: 290px; list-style: none;
  }
  .contact-list li {
    display: flex; align-items: center; gap: 10px; white-space: nowrap;
    font-size: 20px; color: var(--ink); height: 28px;
  }
  .contact-list svg { width: 18px; height: 18px; flex: none; }
  .band-sun {
    position: absolute; left: 0; bottom: 0; width: 320px; height: 16px; background: var(--sun);
  }
  .band-aqua {
    position: absolute; left: 320px; right: 0; bottom: 0; height: 6px; background: var(--aqua);
  }
</style>
</head>
<body>
<main class="canvas">
  <section class="card card-back" aria-label="Card back">
    <div class="pattern" role="img" aria-label="Faint repeating spiral pattern across the card"></div>
    <div class="brand-lockup">
      <span class="brand-mark"></span>
      <span class="brand-name">Brightloom Studios</span>
    </div>
  </section>

  <section class="card card-front" aria-label="Card front">
    <div class="brand-lockup">
      <span class="brand-mark"></span>
      <span class="brand-name">Brightloom Studios</span>
    </div>
    <p class="tagline">Find Your Inner Motion</p>

    <span class="accent-bar"></span>
    <h1 class="person-name">Dana Whitford</h1>
    <p class="person-role">Owner-Operator</p>
    <span class="divider"></span>

    <ul class="contact-list">
      <li>
        <svg viewBox="0 0 24 24" fill="none" stroke="#5ec9d1" stroke-width="2"><circle cx="12" cy="12" r="10"/><path d="M8 7c0 5 4 9 9 10l1-2-3-2-1 1c-2-1-3-2-4-4l1-1-2-3z"/></svg>
        555-014-2290
      </li>
      <li>
        <svg viewBox="0 0 24 24" fill="none" stroke="#5ec9d1" stroke-width="2"><rect x="2" y="5" width="20" height="14"/><path d="M2 5l10 8 10-8"/></svg>
        dana@brightloomstudios.com
      </li>
      <li>
        <svg viewBox="0 0 24 24" fill="none" stroke="#5ec9d1" stroke-width="2"><circle cx="12" cy="12" r="10"/><path d="M2 12h20M12 2c3 3 3 17 0 20M12 2c-3 3-3 17 0 20"/></svg>
        www.brightloomstudios.com
      </li>
    </ul>

    <span class="band-sun"></span>
    <span class="band-aqua"></span>
  </section>
</main>
</body>
</html>
```